Creative, Innovative PowerPoint Sales Deck Refresh needed

We are a technology firm in the Dallas, TX area and we need the powerpoint presentation used for our sales calls refreshed. This presentation is used in one of the first meetings we have with potential clients, so we want to make a memorable and positive impact - we want something that sets us apart from everyone else. We need 8 master slide templates created for our sales deck and a series of slides within the example sales deck need to be completely refreshed (slides 31-37 and 43 in the sample ppt file) We want a sales deck that is modern, innovative, creative, memorable and whimsical - NOT a typical boring "business" design. Colors should match or compliment the colors used in our logo. The logo in the footer of the attached sample ppt is old - it should be replaced with the newer logo attached. Please take a look at our website to get an idea of our culture and aesthetic www.brightkollow.com
Updates

Project Deadline Extended
Reason: We have received several designs we like and we want our entire team to have time to give them full consideration before making a decision.

Target Market(s)

Business executives

Industry/Entity Type

Information Technology

Font styles to use
Sans Serif

Requirements
Must have
• Our logo and LedgerPeak logo in footer
• Master Slide Templates
• Rework / redesign of slides 31-37 and 43
Nice to have
• We use Raleway font in a lot of our materials

```html
<!DOCTYPE html>
<html lang="en">
<head>
<meta charset="utf-8">
<title>Phase One Methodology – Slides 32 to 37</title>
<link href="https://fonts.googleapis.com/css2?family=Raleway:wght@500;600;700&display=swap" rel="stylesheet">
<style>
:root{
  --board:#141b33;
  --board-title:#9aa8a6;
  --slide:#ffffff;
  --band:#1e63a8;
  --heading:#3d3d3d;
  --rule:#cfd8e3;
  --chevron:#a8aaad;
  --blue:#0b66ae;
  --blue-top:#5fa4d6;
  --icon:#9a9c9f;
  --ink:#141414;
  --brand:#1d2a44;
}
*{box-sizing:border-box;margin:0;padding:0}
html,body{width:1200px;height:1200px;overflow:hidden;background:var(--board);font-family:"Raleway",sans-serif}
.board-title{position:absolute;top:40px;left:0;width:1200px;text-align:center;color:var(--board-title);font-size:29px;font-weight:600;letter-spacing:.3px}
.slide{position:absolute;width:589px;height:332px;background:var(--slide);border-top:6px solid var(--band)}
.s1{left:6px;top:138px}.s2{left:605px;top:134px}
.s3{left:6px;top:485px}.s4{left:605px;top:485px}
.s5{left:6px;top:837px}.s6{left:605px;top:837px}
.slide-heading{position:absolute;left:18px;top:12px;font-size:16px;font-weight:700;color:var(--heading);letter-spacing:.2px}
.slide-rule{position:absolute;left:18px;top:35px;width:555px;height:1px;background:var(--rule)}
.phase-track{position:absolute;left:0;top:70px;width:589px;height:40px}
.phase-track text{fill:#fff;font-size:11px;font-weight:600;text-anchor:middle;font-family:"Raleway",sans-serif}
.icon-row{position:absolute;left:0;top:114px;width:589px;height:44px}
.pillars{position:absolute;left:0;top:180px;width:589px;height:100px}
.pillars text{fill:#fff;font-size:11px;font-weight:700;text-anchor:middle;font-family:"Raleway",sans-serif}
.phase-pill{position:absolute;left:65px;top:166px;width:144px;height:30px;border-radius:15px;background:var(--blue);color:#fff;font-size:11.5px;font-weight:600;display:flex;align-items:center;justify-content:center;box-shadow:0 2px 3px rgba(0,0,0,.25)}
.phase-icon{position:absolute;left:116px;top:207px;width:42px;height:42px}
.task-list{position:absolute;left:227px;top:164px;list-style:none}
.task-list li{position:relative;font-size:9.6px;font-weight:600;color:var(--ink);line-height:21.6px;padding-left:12px}
.task-list li::before{content:"•";position:absolute;left:0}
.task-list .sub{font-size:7.6px;line-height:20px;padding-left:48px}
.task-list .sub::before{content:"-";left:36px;color:var(--blue)}
.footer-brand{position:absolute;left:20px;bottom:10px;font-size:12.5px;font-weight:600;color:#333;letter-spacing:-.2px}
.footer-partner{position:absolute;right:17px;bottom:10px;display:flex;align-items:center;gap:4px;font-size:10.5px;font-weight:700;color:var(--brand);letter-spacing:.6px}
.footer-partner::before{content:"";width:12px;height:12px;background:var(--brand)}
</style>
</head>
<body>
<svg width="0" height="0" style="position:absolute">
  <defs>
    <g id="chevrons" fill="var(--chevron)" stroke="#fff" stroke-width="2">
      <polygon points="35,2 132,2 149,20 132,38 35,38 52,20"/>
      <polygon points="135,2 232,2 249,20 232,38 135,38 152,20"/>
      <polygon points="235,2 332,2 349,20 332,38 235,38 252,20"/>
      <polygon points="335,2 432,2 449,20 432,38 335,38 352,20"/>
      <polygon points="435,2 532,2 549,20 532,38 435,38 452,20"/>
    </g>
    <g id="ico-monitor"><circle cx="21" cy="21" r="16" fill="var(--icon)"/><rect x="12" y="13" width="18" height="12" rx="1" fill="#fff"/><rect x="14" y="15" width="14" height="8" fill="var(--icon)"/><rect x="19" y="25" width="4" height="3" fill="#fff"/><rect x="15" y="28" width="12" height="2" fill="#fff"/></g>
    <g id="ico-doc"><rect x="10" y="6" width="18" height="26" fill="var(--icon)"/><g stroke="#fff" stroke-width="1.6"><line x1="13" y1="12" x2="22" y2="12"/><line x1="13" y1="17" x2="25" y2="17"/><line x1="13" y1="22" x2="20" y2="22"/></g><polygon points="22,30 34,18 37,21 25,33 21,34" fill="var(--icon)" stroke="#fff" stroke-width="1"/></g>
    <g id="ico-code" fill="none" stroke="var(--icon)" stroke-width="1.4"><rect x="7" y="8" width="28" height="26"/><line x1="7" y1="13" x2="35" y2="13"/><polyline points="16,19 12,23 16,27"/><polyline points="26,19 30,23 26,27"/><line x1="23" y1="18" x2="19" y2="28"/></g>
    <g id="ico-gear"><path d="M18 6 H30 L36 12 V34 H18 Z" fill="none" stroke="var(--icon)" stroke-width="1.6"/><circle cx="14" cy="28" r="6" fill="var(--icon)"/><g stroke="var(--icon)" stroke-width="3"><line x1="14" y1="19" x2="14" y2="37"/><line x1="5" y1="28" x2="23" y2="28"/><line x1="8" y1="22" x2="20" y2="34"/><line x1="20" y1="22" x2="8" y2="34"/></g><circle cx="14" cy="28" r="2.5" fill="#fff"/></g>
    <g id="ico-support"><rect x="4" y="8" width="26" height="18" fill="none" stroke="var(--icon)" stroke-width="1.6"/><g stroke="var(--icon)" stroke-width="1.4"><line x1="8" y1="13" x2="18" y2="13"/><line x1="8" y1="17" x2="22" y2="17"/><line x1="8" y1="21" x2="15" y2="21"/></g><rect x="2" y="26" width="30" height="3" fill="var(--icon)"/><circle cx="32" cy="22" r="5" fill="var(--icon)"/><path d="M23 36 Q32 24 41 36 Z" fill="var(--icon)"/></g>
  </defs>
</svg>

<h1 class="board-title">SLIDES - 32 to 37 ( Design Idea - 02)</h1>

<section class="slide s1">
  <h2 class="slide-heading">PHASE ONE METHODOLOGY</h2><div class="slide-rule"></div>
  <svg class="phase-track" viewBox="0 0 589 40"><use href="#chevrons"/>
    <text x="92" y="17">Project</text><text x="92" y="31">Initiation</text>
    <text x="192" y="17">Solution</text><text x="192" y="31">Design</text>
    <text x="292" y="17">Application</text><text x="292" y="31">Configuration</text>
    <text x="395" y="17">Testing &amp;</text><text x="395" y="31">Preparation</text>
    <text x="495" y="17">Deployment</text><text x="495" y="31">&amp; Support</text>
  </svg>
  <svg class="icon-row" viewBox="0 0 589 44">
    <use href="#ico-monitor" x="71"/><use href="#ico-doc" x="172"/><use href="#ico-code" x="272"/><use href="#ico-gear" x="374"/><use href="#ico-support" x="474"/>
  </svg>
  <svg class="pillars" viewBox="0 0 589 100">
    <g fill="var(--blue)"><rect x="79" y="12" width="132" height="76"/><ellipse cx="145" cy="88" rx="66" ry="10"/><rect x="228" y="12" width="132" height="76"/><ellipse cx="294" cy="88" rx="66" ry="10"/><rect x="377" y="12" width="132" height="76"/><ellipse cx="443" cy="88" rx="66" ry="10"/></g>
    <g fill="var(--blue-top)" stroke="var(--blue)" stroke-width="1"><ellipse cx="145" cy="12" rx="66" ry="10"/><ellipse cx="294" cy="12" rx="66" ry="10"/><ellipse cx="443" cy="12" rx="66" ry="10"/></g>
    <text x="145" y="52">CHANGE</text><text x="145" y="64">MANAGEMENT</text>
    <text x="294" y="52">USER</text><text x="294" y="64">INVOLVEMENT</text>
    <text x="443" y="52">PROGRAM</text><text x="443" y="64">MANAGEMENT</text>
  </svg>
  <div class="footer-brand">brightkollow</div><div class="footer-partner">LEDGERPEAK</div>
</section>

<section class="slide s2">
  <h2 class="slide-heading">PHASE ONE METHODOLOGY</h2><div class="slide-rule"></div>
  <svg class="phase-track" viewBox="0 0 589 40"><use href="#chevrons"/><text x="92" y="17">Project</text><text x="92" y="31">Initiation</text></svg>
  <div class="phase-pill">Project Initiation</div>
  <svg class="phase-icon" viewBox="0 0 42 42"><use href="#ico-monitor"/></svg>
  <ul class="task-list" style="line-height:20.8px">
    <li>Conduct Kickoff Meeting</li><li>Finalize and Publish Project Schedule</li><li>Requirements Definition and Design</li><li>Requirements Traceability Matrix (RTM) Signoff</li>
  </ul>
  <div class="footer-brand">brightkollow</div><div class="footer-partner">LEDGERPEAK</div>
</section>

<section class="slide s3">
  <h2 class="slide-heading">PHASE ONE METHODOLOGY</h2><div class="slide-rule"></div>
  <svg class="phase-track" viewBox="0 0 589 40"><use href="#chevrons"/><text x="192" y="17">Solution</text><text x="192" y="31">Design</text></svg>
  <div class="phase-pill">Solution Design</div>
  <svg class="phase-icon" viewBox="0 0 42 42"><use href="#ico-doc"/></svg>
  <ul class="task-list">
    <li>Map and Gap Against RTM</li><li>Identify Solutions for Gaps</li>
    <li class="sub">Custom Development</li><li class="sub">Phase Two Initiative</li><li class="sub">Business Process Change</li>
    <li>Business Flow Recommendation</li>
  </ul>
  <div class="footer-brand">brightkollow</div><div class="footer-partner">LEDGERPEAK</div>
</section>

<section class="slide s4">
  <h2 class="slide-heading">PHASE ONE METHODOLOGY</h2><div class="slide-rule"></div>
  <svg class="phase-track" viewBox="0 0 589 40"><use href="#chevrons"/><text x="292" y="17">Application</text><text x="292" y="31">Testing</text></svg>
  <div class="phase-pill">Application Testing</div>
  <svg class="phase-icon" viewBox="0 0 42 42"><use href="#ico-code"/></svg>
  <ul class="task-list">
    <li>System Setup</li><li>Extended Prototyping</li><li>Develop Test Scripts</li><li>Initiate Data Cleansing and Conversion Routines</li>
  </ul>
  <div class="footer-brand">brightkollow</div><div class="footer-partner">LEDGERPEAK</div>
</section>

<section class="slide s5">
  <h2 class="slide-heading">PHASE ONE METHODOLOGY</h2><div class="slide-rule"></div>
  <svg class="phase-track" viewBox="0 0 589 40"><use href="#chevrons"/><text x="395" y="17">Testing &amp;</text><text x="395" y="31">Preparation</text></svg>
  <div class="phase-pill">Testing &amp; Preparation</div>
  <svg class="phase-icon" viewBox="0 0 42 42"><use href="#ico-gear"/></svg>
  <ul class="task-list">
    <li>Unit Testing – Individual modules/functions</li><li>Integration Testing – End-to-End Flow (Order to Cash)</li><li>User Acceptance Testing – Mock Go-Live</li><li>Full Life Cycle Simulations</li><li>End User Training</li>
  </ul>
  <div class="footer-brand">brightkollow</div><div class="footer-partner">LEDGERPEAK</div>
</section>

<section class="slide s6">
  <h2 class="slide-heading">PHASE ONE METHODOLOGY</h2><div class="slide-rule"></div>
  <svg class="phase-track" viewBox="0 0 589 40"><use href="#chevrons"/><text x="495" y="17">Deployment</text><text x="495" y="31">&amp; Support</text></svg>
  <div class="phase-pill">Deployment &amp; Support</div>
  <svg class="phase-icon" viewBox="0 0 42 42"><use href="#ico-support"/></svg>
  <ul class="task-list">
    <li>Setup Production Environment</li><li>Convert Live Data</li><li>GO-LIVE!</li><li>Post Go-Live Support</li><li>Project Closeout</li>
  </ul>
  <div class="footer-brand">brightkollow</div><div class="footer-partner">LEDGERPEAK</div>
</section>
</body>
</html>
```